Squeeze page design

We need to design some squeeze pages for our list building campaigns. We use Ledgerbay as our crm. Our squeeze pages really suck. We simply need to design some pages that look better and will convert, better than what we are currently using.
The landing page that we are trying to replace can be seen at:
http://shieldworksco.example/multi-family-landing-1
The sign up page that we need to replace is:
http://shieldworksco.example/free-multi-family-offer
Our thought is that the landing page and sign up page should be combined into a single squeeze page that will improve conversions - conversions being sign ups.
Updates
Project Deadline Extended
Reason: I have had some requests to extend my deadline and I need to have some updates made to some of the submissions. Thank you.
Industry/Entity Type
Building
Look and feel
Each slider illustrates characteristics of the customer's brand and the style your logo design should communicate.

```html
<!DOCTYPE html>
<html lang="en">
<head>
<meta charset="utf-8">
<title>Shieldworks Co — Multi-Family Security</title>
<link href="https://fonts.googleapis.com/css2?family=Open+Sans:wght@400;600;700&family=Oswald:wght@500;600&display=swap" rel="stylesheet">
<style>
:root{
  --ink:#2b2b2b;
  --muted:#6a6a6a;
  --dark:#1f1f1f;
  --nav:#2a2a2a;
  --blue:#1d86c9;
  --blue-dark:#126aa3;
  --red:#d7262b;
  --hero:#e9ecef;
  --panel:#f3f3f3;
  --line:#d6d6d6;
  --white:#fff;
}
*{box-sizing:border-box;margin:0;padding:0}
html,body{width:1200px;height:2296px;overflow:hidden}
body{font-family:"Open Sans",Arial,sans-serif;color:var(--ink);background:var(--white);font-size:15px}
.wrap{width:960px;margin:0 auto;position:relative}
.topbar{height:24px;background:var(--dark);color:#ccc;font-size:11px}
.topbar .wrap{display:flex;justify-content:space-between;align-items:center;height:24px}
.topbar a{color:#ccc;text-decoration:none;margin-left:14px}
.header{height:96px}
.header .wrap{display:flex;align-items:center;height:96px;gap:24px}
.brand{display:flex;align-items:center;gap:10px;font-weight:700;font-size:22px;color:var(--dark)}
.brand .mark{width:34px;height:34px;background:var(--dark)}
.tagline{font-size:13px;font-weight:600;color:var(--muted);letter-spacing:1px;text-transform:uppercase}
.usa{margin-left:auto;border:2px solid var(--red);color:var(--red);font-family:"Oswald",sans-serif;font-size:18px;padding:6px 14px}
.cart{display:flex;align-items:center;gap:8px;border:1px solid var(--line);padding:8px 12px;font-size:12px;font-weight:600}
.nav{height:28px;background:var(--nav)}
.nav .wrap{display:flex;height:28px;align-items:center}
.nav a{color:#ddd;text-decoration:none;font-size:13px;padding:0 18px;height:28px;line-height:28px}
.nav a.active{background:var(--white);color:var(--dark);font-weight:600}
.hero{height:434px;background:linear-gradient(90deg,#f4f5f7,var(--hero))}
.hero .wrap{height:434px}
.hero h1{position:absolute;left:0;top:70px;font-family:"Oswald",sans-serif;font-weight:600;font-size:62px;color:var(--blue)}
.hero p{position:absolute;left:0;top:170px;width:500px;font-size:21px;line-height:1.45;color:var(--muted)}
.hero .more{position:absolute;left:0;top:310px;font-size:13px;color:var(--blue)}
.hero .photo{position:absolute;right:0;top:0;width:420px;height:434px;background:linear-gradient(180deg,#cfd4d9,#8a8f96)}
.band{height:140px;background:linear-gradient(180deg,var(--blue),var(--blue-dark));color:#fff}
.band .wrap{height:140px}
.band h2{position:absolute;top:18px;left:0;font-size:20px}
.band p{position:absolute;top:48px;left:0;width:620px;font-size:11px;line-height:1.5;color:#dcecf8}
.band .cta{position:absolute;left:0;top:96px;background:var(--red);color:#fff;font-weight:700;font-size:13px;padding:7px 16px}
.band .ship{position:absolute;right:0;top:20px;width:250px;height:100px;text-align:center}
.ship b{display:block;background:#0f5786;font-family:"Oswald",sans-serif;font-size:26px;padding:4px;margin-top:44px}
.ship span{font-size:12px}
.cards{padding:22px 0;height:290px}
.cards .wrap{display:flex;gap:18px}
.card{flex:1;height:246px;border:1px solid var(--line);display:flex;gap:12px;padding:10px}
.card .pic{flex:none;width:140px;height:140px;background:linear-gradient(135deg,#3a3a3a,#6e6e6e)}
.card h3{font-size:15px;margin-bottom:6px}
.card p{font-size:12px;line-height:1.5;color:var(--muted)}
.card a{font-size:12px;color:var(--blue)}
.card.wide .pic{width:100%;height:224px;background:linear-gradient(135deg,#2c2c2c,#7a7a7a)}
.products{height:300px;text-align:center}
.products h2{font-size:18px;padding:12px 0}
.products .row{display:flex;gap:18px}
.product{flex:1;height:230px;background:linear-gradient(135deg,#2e2e2e,#555);position:relative}
.product span{position:absolute;left:12px;bottom:12px;color:#fff;font-family:"Oswald",sans-serif;font-size:20px;text-align:left}
.cols{height:450px;background:var(--panel);padding-top:18px}
.cols .wrap{display:flex;gap:18px}
.col{flex:1;background:var(--white);border:1px solid var(--line);height:410px}
.col h3{font-size:15px;padding:12px 14px;border-bottom:1px solid var(--line)}
.col .body{padding:14px;font-size:12px;line-height:1.55;color:var(--muted)}
.col .body h4{color:var(--ink);font-size:14px;margin-bottom:6px}
.btn-dark{display:inline-block;margin-top:16px;background:var(--dark);color:#fff;padding:6px 12px;font-size:11px}
.acc{border-bottom:1px solid var(--line);padding:10px 14px;font-size:13px;font-weight:600;display:flex;justify-content:space-between}
.acc small{display:block;font-weight:400;color:var(--muted);font-size:11px;margin-top:4px}
.acc i{width:14px;height:14px;border-radius:50%;background:#bbb;flex:none}
.form input{display:block;width:100%;height:26px;border:1px solid var(--line);margin-bottom:8px;padding:0 8px;font-size:11px;font-family:inherit}
.form .btns{display:flex;gap:8px}
.form .btns span{flex:1;text-align:center;color:#fff;padding:7px;font-weight:600}
.press{height:110px;display:flex;align-items:center}
.press .wrap{display:flex;justify-content:space-between}
.press .badge{width:110px;height:44px;background:#c9ccd1}
.footer{height:368px;background:var(--panel);border-top:1px solid var(--line);padding-top:26px}
.footer .wrap{display:flex;gap:40px}
.footer .fcol{flex:1;font-size:12px;line-height:1.9;color:var(--muted)}
.footer h4{color:var(--ink);font-size:14px;margin-bottom:6px}
.bottom{height:56px;background:var(--dark);color:#aaa;font-size:11px;text-align:center;padding-top:10px}
.social{display:flex;justify-content:center;gap:10px;margin-bottom:6px}
.social i{width:18px;height:18px;border-radius:50%;background:#666}
</style>
</head>
<body>
<div class="topbar"><div class="wrap"><span>Customer Service 888-555-0142</span><span><a>FAQ</a><a>Store</a><a>Become a Dealer</a><a>Affiliates</a><a>Login</a></span></div></div>
<header class="header"><div class="wrap">
  <div class="brand"><span class="mark"></span>Shieldworks Co</div>
  <div class="tagline">Built To Protect</div>
  <div class="usa">MADE IN U.S.A</div>
  <div class="cart"><svg width="18" height="16" viewBox="0 0 18 16"><path d="M1 1h3l2 9h9l2-6H5" fill="none" stroke="#333" stroke-width="1.6"/><circle cx="7" cy="14" r="1.5" fill="#333"/><circle cx="14" cy="14" r="1.5" fill="#333"/></svg>Shopping Cart<br>0 items - $0</div>
</div></header>
<nav class="nav"><div class="wrap"><a class="active">Home</a><a>About Us</a><a>Buy Online</a><a>Preventing Break-Ins</a><a>Testimonials</a><a>Our Blog</a><a>Contact Us</a></div></nav>
<section class="hero"><div class="wrap">
  <h1>Why is She Moving?</h1>
  <p>Safety is the #1 reason residents site for moving. Safe communities command higher rents have consistantly higher occupancy.</p>
  <span class="more">Learn More...</span>
  <div class="photo" role="img" aria-label="Photo of a young woman in business attire, looking concerned"></div>
</div></section>
<section class="band"><div class="wrap">
  <h2>Guaranteed to Save You Money!</h2>
  <p>Guaranteed to save you money on security. Safety is the number one reason residents give for moving. We serve the multi-family market, and police recommend our kits. Request a free sample for your property today and see the difference on your doors.</p>
  <span class="cta">FREE SAMPLE - CLICK HERE!</span>
  <div class="ship"><svg width="90" height="40" viewBox="0 0 90 40" style="position:absolute;left:80px;top:0"><rect x="2" y="6" width="54" height="24" fill="#fff"/><path d="M56 12h18l10 10v8H56z" fill="#fff"/><circle cx="18" cy="33" r="5" fill="#0f5786"/><circle cx="70" cy="33" r="5" fill="#0f5786"/></svg><b>FREE SHIPPING</b><span>on orders over $100.00!</span></div>
</div></section>
<section class="cards"><div class="wrap">
  <div class="card"><div class="pic" role="img" aria-label="Kicked-in apartment door"></div><div><h3>Why Secure Your Doors?</h3><p>Safety is the #1 reason residents site for moving. More than 80% of break-ins are through a door.</p><a>Read more...</a></div></div>
  <div class="card wide"><div class="pic" role="img" aria-label="Intruder forcing a front door at night"></div></div>
  <div class="card"><div class="pic" role="img" aria-label="Police officer testing a reinforced door"></div><div><h3>Simply The Best</h3><p>Police Tested and Recommended. Police and other independent sources have thoroughly tested it.</p><a>Read more...</a></div></div>
</div></section>
<section class="products"><div class="wrap">
  <h2>Available For All Doors and Budgets</h2>
  <div class="row">
    <div class="product" role="img" aria-label="Door reinforcement combo kit hardware"><span>EZ Guard<br>Combo Kit</span></div>
    <div class="product" role="img" aria-label="Door jamb repair kit being installed"><span>Jamb Mender</span></div>
    <div class="product" role="img" aria-label="Sliding glass door lock kit"><span>Shield Lock<br>Sliding Glass Doors</span></div>
  </div>
</div></section>
<section class="cols"><div class="wrap">
  <div class="col"><h3>Multi-Family Testimonials</h3><div class="body"><h4>Life is Easier</h4><p>I am a Maintenance Manager in Houston. Things have been getting pretty bad down here for a while and we had been fixing up to 5 kick-ins a week. My owner had me put shields on our entire property about six months ago and we have not had a single problem since.</p><p style="margin-top:8px">By Dana (Austin)</p><span class="btn-dark">View all testimonials</span></div></div>
  <div class="col"><h3>Quick link</h3>
    <div class="acc"><div>We Were Victims<small>In 2008 we were renovating properties when we had a rash of break-ins. After learning one method, we started converting every door we owned.</small></div><i></i></div>
    <div class="acc">Only For Bad Areas?<i></i></div>
    <div class="acc">Intruders Don't Stop Intruders<i></i></div>
    <div class="acc">No Comparison<i></i></div>
  </div>
  <div class="col"><h3>Multi-Family Free Offer</h3><div class="body form">
    <input value="Property Name"><input value="First Name"><input value="Last Name"><input value="Email"><input value="Phone Number"><input value="Number of Units">
    <div class="btns"><span style="background:var(--blue)">Submit</span><span style="background:var(--blue-dark)">Reset</span></div>
  </div></div>
</div></section>
<section class="press"><div class="wrap"><span class="badge"></span><span class="badge"></span><span class="badge"></span><span class="badge"></span><span class="badge"></span><span class="badge"></span><span class="badge"></span></div></section>
<footer class="footer"><div class="wrap">
  <div class="fcol"><h4>Customer Service</h4>Affiliate Program<br>About Us<br>Contact Us<br>Become a Dealer<br>Privacy Policy<br>Warranty Information</div>
  <div class="fcol"><h4>Resources</h4>US Federal Burglary Data<br>Understanding Door Security<br>Crime Prevention Guide<br>National Crime Statistics<br>Department of Justice Notes</div>
  <div class="fcol"><h4>Contact Us</h4>Shieldworks Co, 412 Harlow Ave<br>Brookfield, TN 37000<br>888-555-0142<br>info@shieldworksco.example</div>
</div></footer>
<div class="bottom"><div class="social"><i></i><i></i><i></i><i></i></div>© 2014 Shieldworks Co. All rights reserved.</div>
</body>
</html>
```